Gin Bottle label design

A label for three Gins, 1 Apple flavoured, 1 Bilberry flavoured and one London Dry Gin. All need to incorporate the business logo that i've attached along with the bottle we intend to use. The gin is 40% and will be in a 70cl bottle

```html
<!DOCTYPE html>
<html lang="en">
<head>
<meta charset="utf-8">
<title>Gin Label Range</title>
<link rel="stylesheet" href="https://fonts.googleapis.com/css2?family=Cinzel:wght@400;700&family=Marcellus+SC&family=Montserrat:wght@300&display=swap">
<style>
  :root {
    --burgundy: #6b0d24;
    --cream: #fbf9ea;
    --ink: #141414;
    --rule: #b77b86;
    --sheet: #ffffff;
    --table: #e4e4e4;
    --art-light: #e9e6d6;
    --art-dark: #bdb9a8;
  }
  * { box-sizing: border-box; margin: 0; padding: 0; }
  html, body { width: 800px; height: 1200px; overflow: hidden; }
  body { background: var(--sheet); position: relative; font-family: "Cinzel", serif; }
  .range-band {
    position: absolute; left: 0; top: 875px; width: 800px; height: 325px;
    background: var(--table);
  }
  .label { position: absolute; width: 15em; height: 28em; }
  .label--feature { font-size: 15.3px; left: 294px; top: 334px; }
  .label--left { font-size: 10px; left: 228px; top: 895px; }
  .label--right { font-size: 10px; left: 424px; top: 895px; }

  .label__body {
    position: absolute; inset: 0;
    background: var(--cream);
    border: 0.7em solid var(--burgundy);
    border-radius: 7.5em;
  }
  .label__body::after {
    content: ""; position: absolute; inset: 0.35em;
    border: 1px solid var(--burgundy);
    border-radius: 7em;
  }
  .brand {
    position: absolute; top: 3.6em; left: 0; right: 0;
    display: flex; align-items: center; justify-content: center; gap: 0.4em;
  }
  .brand__dot { width: 0.6em; height: 0.6em; border-radius: 50%; background: var(--burgundy); }
  .brand__name {
    font-size: 0.85em; line-height: 1.1; color: var(--burgundy);
    text-align: center; letter-spacing: 0.04em;
  }
  .art {
    position: absolute; left: 3.6em; right: 3.6em; top: 7.5em; height: 7.6em;
    border-radius: 0.6em;
    background: radial-gradient(ellipse at center, var(--art-dark) 0%, var(--art-light) 65%, var(--cream) 100%);
  }
  .ribbon {
    position: absolute; left: -0.96em; right: -0.96em; top: 15.9em; height: 2em;
    display: flex; align-items: center; justify-content: center; gap: 0.7em;
  }
  .ribbon svg { position: absolute; inset: 0; width: 100%; height: 100%; }
  .ribbon__rule { position: relative; width: 1.8em; height: 1px; background: var(--cream); opacity: 0.8; }
  .ribbon__text {
    position: relative; font-family: "Marcellus SC", serif; color: var(--cream);
    font-size: 0.95em; letter-spacing: 0.03em; white-space: nowrap;
  }
  .spirit, .strength, .volume { position: absolute; left: 0; right: 0; text-align: center; color: var(--ink); }
  .spirit { top: 18em; }
  .spirit__text { display: block; font-size: 5.4em; line-height: 1; font-weight: 400; letter-spacing: -0.01em; }
  .strength { top: 23.65em; }
  .strength__text { display: block; font-family: "Montserrat", sans-serif; font-weight: 300; font-size: 0.7em; line-height: 1; }
  .divider {
    position: absolute; left: 4.6em; right: 4.6em; top: 24.75em; height: 1px;
    background: linear-gradient(90deg, transparent, var(--rule), transparent);
  }
  .volume { top: 25.2em; }
  .volume__text { display: block; font-weight: 700; font-size: 1em; line-height: 1; }
</style>
</head>
<body>
  <div class="range-band"></div>

  <article class="label label--feature">
    <div class="label__body"></div>
    <div class="brand"><span class="brand__dot"></span><span class="brand__name">The Olive<br>Table</span></div>
    <div class="art" role="img" aria-label="Engraved illustration of a whole apple and a halved apple"></div>
    <div class="ribbon">
      <svg viewBox="0 0 170 16" preserveAspectRatio="none" aria-hidden="true"><polygon points="0,0 170,0 164,8 170,16 0,16 6,8" fill="var(--burgundy)"/></svg>
      <span class="ribbon__rule"></span><span class="ribbon__text">Apple Flavoured</span><span class="ribbon__rule"></span>
    </div>
    <div class="spirit"><span class="spirit__text">GIN</span></div>
    <div class="strength"><span class="strength__text">40%</span></div>
    <div class="divider"></div>
    <div class="volume"><span class="volume__text">70CL</span></div>
  </article>

  <article class="label label--left">
    <div class="label__body"></div>
    <div class="brand"><span class="brand__dot"></span><span class="brand__name">The Olive<br>Table</span></div>
    <div class="art" role="img" aria-label="Sketch of a London bridge over the river"></div>
    <div class="ribbon">
      <svg viewBox="0 0 170 16" preserveAspectRatio="none" aria-hidden="true"><polygon points="0,0 170,0 164,8 170,16 0,16 6,8" fill="var(--burgundy)"/></svg>
      <span class="ribbon__rule"></span><span class="ribbon__text">London Dry</span><span class="ribbon__rule"></span>
    </div>
    <div class="spirit"><span class="spirit__text">GIN</span></div>
    <div class="strength"><span class="strength__text">40%</span></div>
    <div class="divider"></div>
    <div class="volume"><span class="volume__text">70CL</span></div>
  </article>

  <article class="label label--right">
    <div class="label__body"></div>
    <div class="brand"><span class="brand__dot"></span><span class="brand__name">The Olive<br>Table</span></div>
    <div class="art" role="img" aria-label="Engraved illustration of bilberries with leaves"></div>
    <div class="ribbon">
      <svg viewBox="0 0 170 16" preserveAspectRatio="none" aria-hidden="true"><polygon points="0,0 170,0 164,8 170,16 0,16 6,8" fill="var(--burgundy)"/></svg>
      <span class="ribbon__rule"></span><span class="ribbon__text">Bilberry Flavoured</span><span class="ribbon__rule"></span>
    </div>
    <div class="spirit"><span class="spirit__text">GIN</span></div>
    <div class="strength"><span class="strength__text">40%</span></div>
    <div class="divider"></div>
    <div class="volume"><span class="volume__text">70CL</span></div>
  </article>
</body>
</html>
```